Wine label Design

We are looking to develop an elegant contemporary Chilean design; for a new Wine Brand TORVANE to be sold in Chinese Market.
We would like to see designs that are a fine balance between having a traditional design that can offer quality reassurance and being distinctive enough to stand out on crowded shelves. The final design should be easy-to-remember and communicate Quality, Tradition and have a conection with Chile.

Target Market(s)

Urban Chinese between 25 to 40 yo

Requirements
Must have
• Paper label
Information on Front label : Grape (example Cabernet sauvignon) / Vintage (ex 2010) / Wine of Chile
Bottle shape is given (see attached)
Nice to have
• An element of uniqueness, easy to recall the brand
Red and Gold Color are appreciated by the Target
Should not have
• White background
Number 4 is considered death, should not be included on the design

```html
<!DOCTYPE html>
<html lang="en">
<head>
<meta charset="utf-8">
<title>TORVANE – Cabernet Sauvignon Label</title>
<link rel="stylesheet" href="https://fonts.googleapis.com/css2?family=Cinzel:wght@600&family=Arimo:wght@700&family=Pinyon+Script&display=swap">
<style>
  :root {
    --backdrop: #1c1c1c;
    --label-red: #b3170e;
    --label-red-deep: #8e0f09;
    --gold: #e3ad2f;
    --gold-light: #f6d374;
    --ink-dark: #3a0805;
  }
  html, body {
    margin: 0;
    padding: 0;
    width: 1200px;
    height: 1025px;
    overflow: hidden;
    background: var(--backdrop);
  }
  .canvas {
    position: relative;
    width: 1200px;
    height: 1025px;
    display: flex;
    align-items: center;
    justify-content: center;
  }
  .front-label {
    position: relative;
    width: 920px;
    height: 620px;
    background: radial-gradient(ellipse at 50% 45%, var(--label-red) 0%, var(--label-red) 45%, var(--label-red-deep) 100%);
    box-sizing: border-box;
  }
  .gold-rule {
    position: absolute;
    left: 0;
    right: 0;
    height: 8px;
    background: linear-gradient(90deg, var(--gold) 0%, var(--gold-light) 50%, var(--gold) 100%);
  }
  .gold-rule--top { top: 14px; }
  .gold-rule--bottom { bottom: 14px; }
  .brand {
    position: absolute;
    left: 90px;
    right: 60px;
    top: 150px;
    display: flex;
    align-items: center;
    justify-content: center;
    gap: 22px;
  }
  .brand-name {
    font-family: "Cinzel", serif;
    font-weight: 600;
    font-size: 118px;
    letter-spacing: 6px;
    line-height: 1;
    color: var(--gold);
  }
  .brand-dot {
    width: 34px;
    height: 34px;
    border-radius: 50%;
    background: var(--gold);
  }
  .details {
    position: absolute;
    left: 0;
    right: 0;
    top: 330px;
    display: flex;
    flex-direction: column;
    align-items: center;
  }
  .detail-line {
    font-family: "Arimo", sans-serif;
    font-weight: 700;
    font-size: 30px;
    letter-spacing: 4px;
    color: var(--ink-dark);
    margin: 0;
    padding: 6px 0;
  }
  .detail-divider {
    width: 360px;
    height: 2px;
    background: var(--ink-dark);
    opacity: 0.7;
  }
  .grape-variety {
    font-family: "Pinyon Script", cursive;
    font-size: 54px;
    color: var(--ink-dark);
    margin: 34px 0 0;
  }
</style>
</head>
<body>
  <main class="canvas">
    <section class="front-label" aria-label="TORVANE front label">
      <div class="gold-rule gold-rule--top"></div>
      <div class="brand">
        <span class="brand-name">TORVANE</span>
        <span class="brand-dot" aria-hidden="true"></span>
      </div>
      <div class="details">
        <p class="detail-line">Vintage 2010</p>
        <div class="detail-divider"></div>
        <p class="detail-line">Wine of Chile</p>
        <p class="grape-variety">Cabernet Sauvignon</p>
      </div>
      <div class="gold-rule gold-rule--bottom"></div>
    </section>
  </main>
</body>
</html>
```